Lumara Health & Wellness Business Card Design

We would like to create business cards matching with our new logo design. The card should be professional looking but still have a playful side and something that would be eye catching. We are planing to open a luxury medical spa and looking to create a design based on this new logo. We are looking for a design that shows off luxury but not be gold in color. Also, while we are a more female oriented medical center we do have men that come in for our services and it should be be too feminine.

Target Market(s)

Health & Wellness. Medical patients. Luxury spa

Industry/Entity Type

Health And Wellness

Contact Information for Business Card

It should have the logo design in the front of card and back of card should have our contact information. Our current colors are peach/ coral, teal, and gray. We are looking for a modern looking design.

Font styles to use
Script

Colors
32a6d6
e667a6
86cfc6
fece3e

Requirements
Must have
• It should have our logo design. We would prefer to have a more modern look to the card.
Nice to have
• Eye-Catching Design on the personable side but still classy.
Should not have
• At this point we are looking for the best design. It should not have color purple.

```html
<!DOCTYPE html>
<html lang="en">
<head>
<meta charset="utf-8">
<title>Lumara Health & Wellness – Business Card</title>
<link rel="stylesheet" href="https://fonts.googleapis.com/css2?family=Great+Vibes&family=Montserrat:wght@400;500&family=Playfair+Display:ital@1&display=swap">
<style>
  :root {
    --backdrop: #000000;
    --ink: #1d1d1f;
    --ink-soft: #444448;
    --marble-light: #fbf8f6;
    --marble-vein: #f2ded6;
    --sky: #32a6d6;
    --aqua: #86cfc6;
    --sun: #fece3e;
    --rose: #e667a6;
    --paper: #ffffff;
  }
  * { margin: 0; padding: 0; box-sizing: border-box; }
  html, body { width: 857px; height: 1200px; overflow: hidden; background: var(--backdrop); }
  .canvas { position: relative; width: 857px; height: 1200px; }
  .card {
    position: absolute; left: 51px; width: 757px; height: 484px; overflow: hidden;
    background: var(--paper);
  }
  .card--front { top: 80px; }
  .card--back { top: 644px; }
  .marble {
    position: absolute; inset: 0;
    background:
      radial-gradient(ellipse at 20% 30%, var(--marble-vein) 0%, transparent 45%),
      radial-gradient(ellipse at 80% 70%, var(--marble-vein) 0%, transparent 40%),
      linear-gradient(135deg, var(--marble-light), #f7ece7 50%, var(--marble-light));
  }
  .accent-band {
    position: absolute; left: 0; width: 757px; height: 64px;
    background: linear-gradient(90deg, var(--sky) 0%, var(--aqua) 40%, var(--sun) 75%);
    opacity: 0.9;
  }
  .card--front .accent-band { top: 232px; }
  .card--back .accent-band { top: 160px; }
  .shapes { position: absolute; inset: 0; }
  .brand {
    position: absolute; font-family: "Great Vibes", cursive; color: var(--ink);
    line-height: 0.95; font-weight: 400;
  }
  .card--front .brand { top: 40px; left: 0; right: 0; text-align: center; font-size: 58px; }
  .card--back .brand { top: 22px; left: 28px; font-size: 44px; }
  .website {
    position: absolute; left: 0; right: 0; text-align: center;
    font-family: "Playfair Display", serif; font-style: italic; font-size: 17px; color: var(--ink);
  }
  .card--front .website { top: 430px; }
  .card--back .website { top: 428px; font-size: 15px; }
  .person { position: absolute; left: 420px; top: 66px; color: var(--ink); }
  .person__name { font-family: "Great Vibes", cursive; font-size: 40px; line-height: 1; }
  .person__role { font-family: "Great Vibes", cursive; font-size: 26px; color: var(--ink-soft); margin-top: 4px; }
  .contact {
    position: absolute; left: 0; right: 0; top: 312px; list-style: none;
    display: flex; flex-direction: column; align-items: center; gap: 12px;
    font-family: "Montserrat", sans-serif; font-size: 14px; color: var(--ink);
  }
  .contact__item { display: flex; align-items: center; gap: 12px; }
  .contact__icon { width: 16px; height: 16px; fill: var(--ink); }
</style>
</head>
<body>
<main class="canvas">

  <section class="card card--front">
    <div class="marble" role="img" aria-label="Soft pink marble texture"></div>
    <div class="accent-band" role="img" aria-label="Flowing ribbon accent in blue, aqua and yellow"></div>
    <div class="brand">Lumara<br>Health &amp; Wellness</div>
    <p class="website">www.lumarawellness.com</p>
  </section>

  <section class="card card--back">
    <div class="marble" role="img" aria-label="Soft pink marble texture"></div>
    <svg class="shapes" viewBox="0 0 757 484" aria-hidden="true">
      <path d="M0 250 L757 250 L757 484 L0 484 Z" fill="var(--rose)"/>
      <path d="M0 250 L757 250 L378 484 Z" fill="var(--paper)"/>
    </svg>
    <div class="accent-band" role="img" aria-label="Flowing ribbon accent in blue, aqua and yellow"></div>
    <div class="brand">Lumara<br>Health &amp; Wellness</div>
    <div class="person">
      <p class="person__name">Name Surname</p>
      <p class="person__role">Job Position</p>
    </div>
    <ul class="contact">
      <li class="contact__item">
        <svg class="contact__icon" viewBox="0 0 16 16" aria-hidden="true"><path d="M8 0a5.5 5.5 0 0 0-5.5 5.5C2.5 10 8 16 8 16s5.5-6 5.5-10.5A5.5 5.5 0 0 0 8 0zm0 7.8a2.3 2.3 0 1 1 0-4.6 2.3 2.3 0 0 1 0 4.6z"/></svg>
        214 Meadow Lane, Suite 4, Fairview, NJ 07022
      </li>
      <li class="contact__item">
        <svg class="contact__icon" viewBox="0 0 16 16" aria-hidden="true"><path d="M1 3h14v10H1z M1.8 3.8 8 8.6l6.2-4.8" fill="none" stroke="var(--ink)" stroke-width="1.4"/></svg>
        info@lumarawellness.com
      </li>
      <li class="contact__item">
        <svg class="contact__icon" viewBox="0 0 16 16" aria-hidden="true"><path d="M3.6 1l2.6 3-1.5 1.8a9 9 0 0 0 5.5 5.5l1.8-1.5 3 2.6-1.8 2.6C7.5 15 1 8.5 1 2.8z"/></svg>
        (555) 014-2270
      </li>
    </ul>
    <p class="website">www.lumarawellness.com</p>
  </section>

</main>
</body>
</html>
```